Accounting business needs business card

I have a business card but need something better. I want the colour changed and the design to be better. I have uploaded a picture of my new sign that is grey in colour, i would like to incorporate these colours.

```html
<!DOCTYPE html>
<html lang="en">
<head>
<meta charset="utf-8">
<title>Even Tax – Business Card</title>
<link rel="stylesheet" href="https://fonts.googleapis.com/css2?family=Open+Sans:wght@400;700&display=swap">
<style>
  :root {
    --lime: #b5c724;
    --card-grey: #d8d9db;
    --ink: #2b2d31;
    --page: #ecebe8;
    --white: #f4f4f4;
    --badge-neutral: #b9bbbf;
  }
  * { box-sizing: border-box; margin: 0; padding: 0; }
  html, body {
    width: 1200px; height: 1169px; overflow: hidden;
    background: var(--page);
    font-family: "Open Sans", sans-serif;
    color: var(--ink);
  }
  .canvas { position: relative; width: 1200px; height: 1169px; }
  .card {
    position: absolute; left: 170px; width: 860px; height: 490px;
    overflow: hidden;
    box-shadow: 0 10px 30px rgba(0,0,0,0.12);
  }
  /* Front */
  .card-front { top: 70px; background: var(--lime); }
  .front-stripe {
    position: absolute; left: 0; right: 0; bottom: 58px; height: 22px;
    background: var(--white);
  }
  .front-mark {
    position: absolute; left: 0; right: 0; top: 95px;
    display: flex; flex-direction: column; align-items: center; gap: 26px;
  }
  .mark-circle {
    width: 130px; height: 130px; border-radius: 50%;
    border: 3px solid var(--ink);
  }
  .wordmark {
    font-weight: 700; font-size: 46px; letter-spacing: 26px;
    color: var(--ink); padding-left: 26px; white-space: nowrap;
  }
  /* Back */
  .card-back { top: 610px; background: var(--lime); padding: 14px; }
  .back-face {
    position: relative; width: 100%; height: 100%;
    background: var(--card-grey); overflow: hidden;
  }
  .back-wave { position: absolute; left: 0; bottom: 0; width: 100%; height: 100%; }
  .back-mark {
    position: absolute; left: 40px; top: 70px; width: 300px;
    display: flex; flex-direction: column; align-items: center; gap: 18px;
  }
  .back-mark .mark-circle { width: 92px; height: 92px; border-width: 2.5px; }
  .back-mark .wordmark { font-size: 28px; letter-spacing: 14px; padding-left: 14px; }
  .divider {
    position: absolute; left: 368px; top: 56px; width: 2px; height: 220px;
    background: var(--lime);
  }
  .details { position: absolute; left: 400px; top: 52px; right: 30px; }
  .person-name { font-weight: 700; font-size: 36px; color: var(--lime); line-height: 1.1; }
  .credentials, .role { font-size: 19px; line-height: 1.3; }
  .contacts { list-style: none; margin-top: 18px; }
  .contacts li {
    display: flex; align-items: center; gap: 14px;
    font-size: 20px; line-height: 1.75;
  }
  .contacts svg { width: 22px; height: 22px; flex: none; }
  .badges {
    position: absolute; left: 400px; top: 300px;
    display: flex; align-items: center; gap: 28px;
  }
  .badge {
    width: 110px; height: 52px; border-radius: 6px;
    background: var(--badge-neutral);
  }
</style>
</head>
<body>
<main class="canvas">

  <section class="card card-front" aria-label="Card front">
    <div class="front-mark">
      <div class="mark-circle"></div>
      <div class="wordmark">EVEN TAX</div>
    </div>
    <div class="front-stripe"></div>
  </section>

  <section class="card card-back" aria-label="Card back">
    <div class="back-face">
      <svg class="back-wave" viewBox="0 0 832 462" preserveAspectRatio="none" aria-hidden="true">
        <path d="M0 300 C 180 300, 300 420, 470 445 C 620 466, 760 450, 832 440 L832 462 L0 462 Z" fill="var(--lime)"/>
        <path d="M0 282 C 190 272, 310 400, 480 432 C 620 456, 760 446, 832 436" fill="none" stroke="var(--ink)" stroke-width="5"/>
      </svg>

      <div class="back-mark">
        <div class="mark-circle"></div>
        <div class="wordmark">EVEN TAX</div>
      </div>

      <div class="divider"></div>

      <div class="details">
        <h1 class="person-name">Dana Whitfield</h1>
        <p class="credentials">CPA, MTAX, BCOM (Acc &amp; Fin)</p>
        <p class="role">Taxation and Business Accountant</p>
        <ul class="contacts">
          <li>
            <svg viewBox="0 0 24 24" aria-hidden="true"><path d="M6.6 10.8a15 15 0 0 0 6.6 6.6l2.2-2.2a1 1 0 0 1 1-.25 11.4 11.4 0 0 0 3.6.57 1 1 0 0 1 1 1V20a1 1 0 0 1-1 1A17 17 0 0 1 3 4a1 1 0 0 1 1-1h3.5a1 1 0 0 1 1 1c0 1.25.2 2.45.57 3.57a1 1 0 0 1-.25 1z" fill="var(--lime)"/></svg>
            0412 555 309
          </li>
          <li>
            <svg viewBox="0 0 24 24" aria-hidden="true"><rect x="2" y="5" width="20" height="14" fill="none" stroke="var(--lime)" stroke-width="2.4"/><path d="M2 5l10 8 10-8" fill="none" stroke="var(--lime)" stroke-width="2.4"/></svg>
            dana@eventax.com.au
          </li>
          <li>
            <svg viewBox="0 0 24 24" aria-hidden="true"><circle cx="12" cy="12" r="11" fill="var(--lime)"/><g fill="none" stroke="var(--card-grey)" stroke-width="1.3"><ellipse cx="12" cy="12" rx="4" ry="8"/><path d="M4 12h16M5.5 8h13M5.5 16h13"/></g></svg>
            www.eventax.com.au
          </li>
        </ul>
      </div>

      <div class="badges">
        <div class="badge" role="img" aria-label="Professional membership badge"></div>
        <div class="badge" role="img" aria-label="Software partner badge"></div>
      </div>
    </div>
  </section>

</main>
</body>
</html>
```